Premium Personal Brand — Facebook Banner (Used Across All Platforms)

Update — Additional Color Direction
In addition to the dark charcoal/slate direction already described, I'm also interested in seeing variants with:
Dark navy blue — Deep, authoritative, intelligence-community feel. Same textured/matte treatment, not flat or bright.
Warm charcoal with steel blue accent — Keep the dark base but introduce a subtle steel blue gradient, accent line, or tonal shift. Sophisticated, modern, adds dimension without adding color noise.
Both should maintain the same premium, restrained, architectural feel described in the original brief. No bright blues, no corporate PowerPoint energy — think midnight, think depth, think weight.
Everything else in the brief remains the same.
I am building a premium personal brand as an executive advisor to founders ($5M+ revenue).
This contest is Facebook-banner–focused, but the design must represent a visual system that will be reused across:
- LinkedIn
- YouTube
I- nstagram
- X (Twitter)
- Website hero sections and other brand touchpoints
Think of the Facebook banner as the primary expression of the brand — not a one-off graphic.
This project is about discovering a high-end visual style and brand feel, not decoration.
What to design
Please submit one cohesive visual system, shown primarily as:
- Facebook banner (primary focus)
The same design language should clearly translate to all platforms listed above.
Designers are responsible for using the current recommended dimensions for each platform.
Quick clarification on background direction:
Backgrounds should have depth and texture, not flat color fields. Avoid pure white, light grey, or solid black backgrounds. Think matte, architectural materials — stone, graphite, concrete, steel — not blank canvases. Subtle tonal variation is encouraged. Obvious gradients or decorative patterns are not.
Text to use
Primary Headline:
- Your Business Is Too Valuable To Be Run On Hope.
Subheadline:
- You didn’t build a business to become its prisoner.
Name:
Milo Verant
The headline should be the dominant visual element.
Logo note (important)
My personal logo is currently being finalized.
For this contest:
- Use a simple “MV” monogram placeholder
- Clean, bold, geometric sans-serif
- Do not design a logo
- The winning design must allow an easy logo swap later.
Headshot note (important)
- Please do not include a headshot in the banner design.
- Most platforms display a circular profile image separately.
- The banner should stand on its own using typography, layout, and tone only.
- Design the banner assuming the profile photo will sit nearby, not inside the banner.
Style direction
The design should feel:
- Premium
- Calm
- Confident
- Restrained
- High-trust
- Dark, neutral backgrounds are preferred.
- Fewer elements are better than more.
Think:
- Owner-level advisor
- Private equity / boardroom tone
- Industrial, Modern, Minimalist, Elite, Architectural, not decorative
What to avoid
Please do not submit designs that feel:
- Promotional, hype-driven, or salesy
- Like a coach, guru, or agency
- Bright, colorful, or gradient-heavy
- Busy or over-designed
- Based on stock photos
- No motivational speaker energy.
Reaction test
- If someone sees this banner on Facebook (or later on LinkedIn, YouTube, etc.), the reaction should be:
“That person is serious. I’d trust them with important decisions.”
Final note
- I am not looking for many variations.
- I am looking for one strong visual direction you believe in.
Simple beats clever.
- Restraint beats decoration.

```html
<!DOCTYPE html>
<html lang="en">
<head>
<meta charset="UTF-8">
<title>Milo Verant — Banner</title>
<link rel="stylesheet" href="https://fonts.googleapis.com/css2?family=Montserrat:wght@300;500;700&display=swap">
<style>
  :root {
    --page: #ffffff;
    --slate-light: #2c2c2c;
    --slate-mid: #222222;
    --slate-deep: #161616;
    --ink: #ffffff;
    --ink-soft: #f1f1f1;
  }
  * { margin: 0; padding: 0; box-sizing: border-box; }
  html, body {
    width: 1200px;
    height: 700px;
    overflow: hidden;
    background: var(--page);
  }
  .canvas {
    position: relative;
    width: 1200px;
    height: 700px;
    background: var(--page);
  }
  .banner {
    position: absolute;
    left: 70px;
    top: 118px;
    width: 1060px;
    height: 464px;
    overflow: hidden;
    font-family: 'Montserrat', sans-serif;
    color: var(--ink);
  }
  .banner-surface {
    position: absolute;
    inset: 0;
    background:
      radial-gradient(ellipse at 55% 30%, var(--slate-light) 0%, rgba(44,44,44,0) 60%),
      radial-gradient(ellipse at 8% 30%, #303030 0%, rgba(48,48,48,0) 35%),
      linear-gradient(180deg, var(--slate-mid) 0%, var(--slate-deep) 100%);
  }
  .headline {
    position: absolute;
    left: 0;
    right: 0;
    top: 190px;
    text-align: center;
    font-weight: 700;
    font-size: 31px;
    letter-spacing: 0.01em;
    line-height: 1.2;
  }
  .subheadline {
    position: absolute;
    left: 0;
    right: 0;
    top: 250px;
    text-align: center;
    font-weight: 500;
    font-size: 18.5px;
    letter-spacing: 0.07em;
    color: var(--ink-soft);
  }
  .signature {
    position: absolute;
    left: 0;
    right: 0;
    top: 386px;
    display: flex;
    justify-content: center;
    align-items: center;
    gap: 13px;
  }
  .monogram {
    font-weight: 700;
    font-size: 25px;
    letter-spacing: -0.01em;
  }
  .name {
    font-weight: 300;
    font-size: 17px;
    letter-spacing: 0.02em;
  }
</style>
</head>
<body>
  <main class="canvas">
    <section class="banner">
      <div class="banner-surface" role="img" aria-label="Dark scratched slate texture background"></div>
      <h1 class="headline">Your Business Is Too Valuable To Be Run On Hope.</h1>
      <p class="subheadline">You didn’t build a business to become its prisoner.</p>
      <div class="signature">
        <span class="monogram">MV</span>
        <span class="name">Milo Verant</span>
      </div>
    </section>
  </main>
</body>
</html>
```